VelloCap Nutrition Require Label Design Assistance

We are VelloCap!

We are a new mushroom focused nutrition supplement company looking for some design assistance. We are looking to provide some of the highest quality mushroom supplements available on the market today, using 100% fruiting bodies where many other companies opt for cheaper alternatives. We strongly believe in the power of mushroom nutrition and wish to focus on the high-end supplement market.

We are starting with three initial ranges; Lions Mane, Turkey Tail and Reishi - and wish to have powerful yet elegant designs for each. We wish to be visually appealing whilst maintaining the high-end feel. Imagery of the mushrooms on the label would be good if it maintains high-end appeal. Our bottles will be dark green and lids will be white if this helps with visualization. We have a logo and preferred font for the name which can be used if possible. The image in the logo may need resizing to fit with the supplement market (smaller logo/larger font). If you provide a superior logo to that which we currently have, we would consider using it.

The three range designs should be the same, but with the mushroom name and any imagery changed to reflect the different ranges. I am happy to supply images where required.

Label dimensions = 55mm x 150mm

Target Market(s)

Premium High End Health Supplements

Industry/Entity Type

Supplement

Font styles to use
Serif
Sans Serif

Colors

Designer to choose colors to be used in the design.

Requirements
Must have
• Must have the text "100% Fruiting Bodies"
• Must have Organic + Vegan notification.
• Must have an ingredients section, and there will need to be some space for small-print (which will be decided on shortly).
Nice to have
• See label specifications in message thread.

```html
<!DOCTYPE html>
<html lang="en">
<head>
<meta charset="UTF-8">
<title>VelloCap Organic Mushroom Label</title>
<link href="https://fonts.googleapis.com/css2?family=Oswald:wght@300;400;500;600&display=swap" rel="stylesheet">
<style>
  :root {
    --canvas: #f2f2f4;
    --ink: #23242e;
    --silver-dark: #c9cacd;
    --silver-light: #f5f5f6;
    --silver-text: #d6d7da;
    --gold-dark: #8a7340;
    --gold-mid: #d9c68f;
    --gold-light: #f1e9cc;
    --panel-gold-a: #b8a26a;
    --panel-gold-b: #efe7ca;
  }
  * { margin: 0; padding: 0; box-sizing: border-box; }
  html, body { width: 1200px; height: 1200px; overflow: hidden; background: var(--canvas); }
  body { position: relative; font-family: "Oswald", sans-serif; }

  .label {
    position: absolute; left: 126px; top: 36px;
    width: 948px; height: 1128px;
    background: var(--ink);
  }
  .side-rail {
    position: absolute; left: 4px; top: 18px; width: 12px; height: 996px;
    background: linear-gradient(90deg, #8d8e93, #d9dadd, #8d8e93);
  }
  .side-title {
    position: absolute; left: 74px; top: 396px;
    transform: translate(-50%, -50%) rotate(-90deg);
    white-space: nowrap;
    font-size: 50px; font-weight: 400; letter-spacing: 4px;
    color: var(--silver-text);
  }
  .main-panel {
    position: absolute; left: 122px; top: 16px; width: 808px; height: 998px;
    background: linear-gradient(90deg, var(--silver-dark), var(--silver-light) 40%, var(--silver-light) 60%, var(--silver-dark));
  }
  .brand {
    position: absolute; left: 40px; top: 30px; height: 110px;
    display: flex; align-items: center; gap: 28px;
  }
  .brand-dot { width: 84px; height: 84px; border-radius: 50%; border: 5px solid var(--ink); }
  .brand-name {
    font-size: 78px; font-weight: 300; letter-spacing: 12px;
    color: var(--ink); text-transform: uppercase;
  }
  .brand-rule {
    position: absolute; left: 4px; top: 136px; width: 794px; height: 7px; background: var(--ink);
  }
  .range-line {
    position: absolute; left: 0; width: 808px; top: 182px;
    text-align: center; font-size: 86px; font-weight: 600; letter-spacing: 1px;
    color: var(--ink); line-height: 1;
  }
  .gold-text {
    background: linear-gradient(90deg, var(--gold-dark), var(--gold-mid) 45%, var(--gold-light) 55%, var(--gold-dark));
    -webkit-background-clip: text; background-clip: text; color: transparent;
  }
  .product-band {
    position: absolute; left: 0; top: 302px; width: 798px; height: 162px;
    background: var(--ink);
    display: flex; align-items: center; justify-content: center;
  }
  .product-name {
    font-size: 148px; font-weight: 500; line-height: 1; letter-spacing: 2px;
    color: #e3e4e7; margin-left: -40px;
  }
  .fruiting {
    position: absolute; left: 0; top: 488px; width: 808px;
    display: flex; align-items: center; justify-content: center; gap: 14px;
  }
  .fruiting-dash { width: 66px; height: 5px; background: var(--ink); }
  .fruiting-text { font-size: 66px; font-weight: 600; line-height: 1.1; }
  .dotted-rule {
    position: absolute; left: 46px; width: 738px; height: 0;
    border-top: 4px dotted var(--ink);
  }
  .dotted-rule.top { top: 582px; }
  .dotted-rule.bottom { top: 662px; }
  .purity {
    position: absolute; left: 0; top: 598px; width: 808px;
    text-align: center; font-size: 40px; font-weight: 500; color: var(--ink);
    letter-spacing: 1px; line-height: 1.2;
  }
  .feature-panel {
    position: absolute; left: 8px; top: 684px; width: 788px; height: 308px;
    background: linear-gradient(90deg, var(--panel-gold-a), var(--panel-gold-b) 45%, var(--panel-gold-b) 70%, var(--panel-gold-a));
  }
  .feature-list {
    position: absolute; left: 142px; top: 26px;
    font-size: 44px; font-weight: 500; line-height: 50px; color: var(--ink);
  }
  .feature-list .diet-note {
    display: block; margin-top: 6px;
    font-size: 32px; font-weight: 600; letter-spacing: 1px; color: var(--gold-dark);
  }
  .mushroom-art {
    position: absolute; left: 458px; top: 12px; width: 318px; height: 284px;
    background:
      radial-gradient(circle at 45% 25%, #e06a3a 0, #c8502c 22%, transparent 40%),
      radial-gradient(circle at 78% 75%, #f4f1ea 0, #e8e2d4 22%, transparent 38%),
      radial-gradient(circle at 28% 72%, #8c6a52 0, #6e5040 22%, transparent 40%);
  }
  .count-badge {
    position: absolute; left: 64px; top: 774px; width: 188px; height: 200px;
    background: linear-gradient(180deg, var(--silver-light), var(--silver-dark));
    border: 4px solid var(--ink); outline: 3px solid var(--silver-light); outline-offset: 3px;
    box-shadow: inset 0 0 0 5px var(--silver-light), inset 0 0 0 8px var(--ink);
    text-align: center; color: var(--ink);
  }
  .count-number { display: block; font-size: 118px; font-weight: 600; line-height: 1; margin-top: 12px; }
  .count-unit { display: block; font-size: 30px; font-weight: 400; margin-top: 4px; }
  .footer-spec {
    position: absolute; left: 0; top: 1022px; width: 948px;
    text-align: center; font-size: 34px; font-weight: 500; color: var(--silver-text);
    letter-spacing: 1px; line-height: 1.3;
  }
  .ingredients {
    position: absolute; left: 40px; top: 1074px; width: 868px;
    text-align: center; font-size: 19px; font-weight: 400; color: var(--silver-text);
    letter-spacing: 0.5px; line-height: 1.3;
  }
  .ingredients strong { font-weight: 600; }
</style>
</head>
<body>
  <div class="label">
    <div class="side-rail"></div>
    <div class="side-title">DIETARY SUPPLEMENT</div>

    <div class="main-panel">
      <div class="brand">
        <span class="brand-dot"></span>
        <span class="brand-name">VelloCap</span>
      </div>
      <div class="brand-rule"></div>

      <div class="range-line">ORGANIC <span class="gold-text">MUSHROOM</span></div>

      <div class="product-band"><span class="product-name">TRIVALE</span></div>

      <div class="fruiting">
        <span class="fruiting-dash"></span>
        <span class="fruiting-text gold-text">100% FRUITING BODIES</span>
        <span class="fruiting-dash"></span>
      </div>

      <div class="dotted-rule top"></div>
      <div class="purity">· NO MYCELIUM · NO FILLERS ·</div>
      <div class="dotted-rule bottom"></div>

      <div class="feature-panel">
        <div class="feature-list">MUSHROOM<br>SUPERFOOD<br>DAILY BOOST<br>CAPSULES<span class="diet-note">ORGANIC + VEGAN</span></div>
        <div class="mushroom-art" role="img" aria-label="Photo of reishi, turkey tail and lion's mane mushrooms"></div>
      </div>
    </div>

    <div class="count-badge">
      <span class="count-number">60</span>
      <span class="count-unit">CAPSULES</span>
    </div>

    <div class="footer-spec">60 CAPSULES | 735 MG PER CAPSULE</div>
    <div class="ingredients"><strong>INGREDIENTS:</strong> Organic reishi, turkey tail and lion's mane fruiting body powder. Vegan pullulan capsule. Take 2 capsules daily with water.</div>
  </div>
</body>
</html>
```